Tranvik Leasing Corp - Business Card Design

Need a new modern designed business card that is different and stands out to represent my equipment financing company. Tranvik Leasing Corp finances all types of equipment and all types of industries. We like to do equipment financing a different way by putting customers first and want our card to represent that different approach to business. I want a card that some remembers when they receive it so it sticks in their mind and makes that wow impression.

Card should have a black background so the logo stands out. It can be horizontial or vertical or a combination of both.

Front of card information is below that shows the information that would go on my card. That is where I want a different look or design to stand out. The front could be split black/orange colour so the logo could pop on black side and information on orange side with different lettering. Just outside the box thinking on the front of the card. Open to any type of design.

Back of card is below which i I like unless you have a different spin to provide or a different idea that would make the card better as I am open to anything that looks great.

Target Market(s)

Tranvik Leasing Corp deals with business owners in all industries.

Industry/Entity Type

Business

Contact Information for Business Card

Colors

Designer to choose colors to be used in the design.

Requirements
Must have
• Modern
• Different
• Stand Out
• Makes an Impression

```html
<!DOCTYPE html>
<html lang="en">
<head>
<meta charset="UTF-8">
<title>Tranvik Leasing Corp – Business Card</title>
<link href="https://fonts.googleapis.com/css2?family=Lato:wght@400;700;900&display=swap" rel="stylesheet">
<style>
  :root {
    --canvas-bg: #1b1b1d;
    --card-top: #262628;
    --card-bottom: #101011;
    --orange: #f0642a;
    --orange-light: #f7993a;
    --text-light: #e9e9e9;
    --text-muted: #cfcfcf;
  }
  * { box-sizing: border-box; margin: 0; padding: 0; }
  html, body {
    width: 1200px;
    height: 900px;
    overflow: hidden;
    background: var(--canvas-bg);
    font-family: "Lato", sans-serif;
  }
  .canvas {
    position: relative;
    width: 1200px;
    height: 900px;
    display: flex;
    flex-direction: column;
    align-items: center;
    justify-content: center;
    gap: 40px;
  }
  .card {
    position: relative;
    width: 700px;
    height: 400px;
    background: linear-gradient(160deg, var(--card-top), var(--card-bottom));
    box-shadow: 0 14px 30px rgba(0,0,0,0.55);
    overflow: hidden;
  }

  /* Front */
  .contact-rail {
    position: absolute;
    left: 68px;
    top: 0;
    width: 2px;
    height: 330px;
    background: var(--orange);
  }
  .contact-list {
    position: absolute;
    left: 52px;
    top: 150px;
    list-style: none;
    display: flex;
    flex-direction: column;
    gap: 14px;
  }
  .contact-item {
    display: flex;
    align-items: center;
    gap: 18px;
    color: var(--text-muted);
    font-size: 17px;
    letter-spacing: 0.3px;
  }
  .contact-icon {
    width: 34px;
    height: 34px;
    border-radius: 50%;
    background: var(--orange);
    display: flex;
    align-items: center;
    justify-content: center;
    flex-shrink: 0;
  }
  .contact-icon svg { width: 18px; height: 18px; }

  .person {
    position: absolute;
    right: 60px;
    top: 120px;
    text-align: right;
  }
  .person-name {
    font-weight: 900;
    font-size: 36px;
    color: var(--orange);
    letter-spacing: 0.5px;
    text-transform: uppercase;
  }
  .person-title {
    font-weight: 400;
    font-size: 20px;
    color: var(--text-light);
    letter-spacing: 1px;
    text-transform: uppercase;
  }

  .brand {
    position: absolute;
    display: flex;
    align-items: center;
    gap: 12px;
    font-weight: 700;
    color: var(--orange-light);
    text-transform: uppercase;
    letter-spacing: 2px;
  }
  .brand-dot {
    border-radius: 50%;
    background: var(--orange);
  }
  .card-front .brand {
    right: 60px;
    bottom: 50px;
    font-size: 18px;
  }
  .card-front .brand-dot { width: 14px; height: 14px; }

  /* Back */
  .card-back {
    display: flex;
    align-items: center;
    justify-content: center;
  }
  .card-back .brand {
    position: static;
    font-size: 28px;
    letter-spacing: 3px;
  }
  .card-back .brand-dot { width: 22px; height: 22px; }
</style>
</head>
<body>
<main class="canvas">
  <section class="card card-front" aria-label="Card front">
    <div class="contact-rail"></div>
    <ul class="contact-list">
      <li class="contact-item">
        <span class="contact-icon">
          <svg viewBox="0 0 24 24" fill="none" stroke="#fff" stroke-width="2">
            <rect x="7" y="2" width="10" height="20" rx="2"/>
            <line x1="11" y1="18" x2="13" y2="18"/>
          </svg>
        </span>
        403.555.0192
      </li>
      <li class="contact-item">
        <span class="contact-icon">
          <svg viewBox="0 0 24 24" fill="none" stroke="#fff" stroke-width="2">
            <rect x="3" y="5" width="18" height="14" rx="1"/>
            <polyline points="3,6 12,13 21,6"/>
          </svg>
        </span>
        dana@tranvikleasing.ca
      </li>
      <li class="contact-item">
        <span class="contact-icon">
          <svg viewBox="0 0 24 24" fill="none" stroke="#fff" stroke-width="2">
            <circle cx="12" cy="12" r="9"/>
            <ellipse cx="12" cy="12" rx="4" ry="9"/>
            <line x1="3" y1="12" x2="21" y2="12"/>
          </svg>
        </span>
        www.tranvikleasing.ca
      </li>
    </ul>

    <div class="person">
      <p class="person-name">Dana Mercer</p>
      <p class="person-title">President</p>
    </div>

    <div class="brand">
      <span class="brand-dot"></span>
      <span class="brand-name">Tranvik Leasing Corp</span>
    </div>
  </section>

  <section class="card card-back" aria-label="Card back">
    <div class="brand">
      <span class="brand-dot"></span>
      <span class="brand-name">Tranvik Leasing Corp</span>
    </div>
  </section>
</main>
</body>
</html>
```